Design a Wordpress Mockup for Pet Food Website

I have a pet food related site that needs new look and design. I am looking for UI improvement of this wordpress website.
Here is the link http://qzv.ly/48tzpq

```html
<!DOCTYPE html>
<html lang="en">
<head>
<meta charset="utf-8">
<title>VitalPawsLife – Pet Food</title>
<link href="https://fonts.googleapis.com/css2?family=Roboto:wght@400;500;700&display=swap" rel="stylesheet">
<style>
:root{
  --page:#f2f2f2;
  --white:#ffffff;
  --blue:#3b98f0;
  --pink:#f0306a;
  --teal:#1cbfbf;
  --ink:#333333;
  --muted:#666666;
  --rule:#dddddd;
  --footer:#e4e6ea;
}
*{box-sizing:border-box;margin:0;padding:0}
html,body{width:1200px;height:2387px;overflow:hidden}
body{background:var(--page);font-family:'Roboto',Arial,sans-serif;color:var(--ink);position:relative}
.abs{position:absolute}
a{color:inherit;text-decoration:none}

.topbar{left:0;top:0;width:1200px;height:47px;border-bottom:1px solid var(--rule)}
.topbar .phone{left:766px;top:10px;display:flex;align-items:center;gap:10px;font-size:13px;color:var(--muted)}
.topbar .cart{left:973px;top:10px;display:flex;align-items:center;gap:10px;font-size:13px;color:var(--muted)}

.brand{left:120px;top:86px;font-size:36px;font-weight:700;color:#1d5c8f;letter-spacing:-0.5px;display:flex;align-items:center;gap:10px}
.brand .dot{width:14px;height:14px;border-radius:50%;background:var(--teal)}

.search{left:823px;top:101px;width:257px;height:35px;display:flex}
.search input{flex:1;border:none;background:var(--white);padding:0 16px;font:13px 'Roboto',sans-serif;color:var(--muted)}
.search button{width:34px;border:none;background:#333;display:flex;align-items:center;justify-content:center}

.nav{left:119px;top:169px;width:960px;height:56px;background:var(--blue);display:flex;align-items:center;padding-left:10px}
.nav a{color:var(--white);font-size:15px;padding:0 32px;border-right:1px solid rgba(255,255,255,.45);line-height:24px}
.nav a:last-child{border-right:none}

.slider{left:120px;top:253px;width:609px;height:418px;background:var(--white)}
.slider .photo{position:absolute;left:0;top:30px;width:609px;height:300px;background:linear-gradient(180deg,#ffffff,#5a524d 45%,#2c2826 70%,#ffffff)}
.slider .arrow{position:absolute;top:186px;width:45px;height:45px;background:var(--pink);display:flex;align-items:center;justify-content:center}

.promo{left:756px;width:323px;background:var(--white)}
.promo .photo{height:148px}
.promo .band{height:44px;display:flex;align-items:center;padding:0 12px 0 18px;color:var(--white)}
.promo .band strong{font-size:17px;font-weight:700;width:100px}
.promo .band span{font-size:10px;line-height:12px;flex:1}
.promo .band i{width:32px;height:32px;border-radius:50%;background:var(--white);display:flex;align-items:center;justify-content:center}

.product{left:120px;width:620px;height:256px}
.product .photo{position:absolute;left:0;top:0;width:254px;height:256px}
.product h3{position:absolute;left:278px;top:2px;font-size:18px;font-weight:400;color:#222}
.product p{position:absolute;left:278px;top:32px;width:290px;font-size:10.5px;line-height:22.5px;color:var(--muted)}
.btn{display:inline-flex;align-items:center;justify-content:center;background:var(--pink);color:var(--white);font-size:18px;width:168px;height:43px}
.product .btn{position:absolute;left:279px}

.panel{left:756px;width:323px;background:var(--white)}
.panel .head{height:40px;background:var(--teal);color:var(--white);font-size:18px;padding:9px 24px}
.panel h4{font-size:16.5px;font-weight:400;color:#222;margin:0 0 6px 0}
.panel ul{list-style:none}
.panel li{font-size:10.5px;line-height:22.6px;color:var(--muted);padding-left:22px;position:relative}
.panel li::before{content:"";position:absolute;left:2px;top:8px;width:7px;height:7px;border-radius:50%;background:var(--pink)}

.poll p{font-size:11.5px;color:#444}
.poll label{display:flex;gap:10px;font-size:10px;color:var(--muted);line-height:13px;max-width:230px}
.poll label i{flex:none;width:11px;height:11px;border:1px solid #aaa;border-radius:50%;margin-top:1px}

.tile{top:1941px;width:292px;height:166px;display:flex;align-items:center;padding-left:22px;gap:16px;color:var(--white)}
.tile strong{display:block;font-size:23px;font-weight:700}
.tile span{display:block;font-size:13px;font-weight:700;line-height:23px;margin-top:4px}

.footer{left:0;top:2149px;width:1200px;height:238px;background:var(--footer)}
.footer h5{position:absolute;top:38px;font-size:12.5px;font-weight:700;color:#333;letter-spacing:.3px}
.footer ul{position:absolute;top:76px;list-style:none}
.footer li{font-size:12px;line-height:22.6px;color:var(--muted)}
.footer .social{position:absolute;left:746px;top:70px;display:flex;gap:9px}
.footer .social i{width:29px;height:29px;border-radius:50%;background:#555}
.footer .badge{position:absolute;left:740px;top:126px;width:66px;height:66px;border-radius:50%;background:#7a4a22}
.footer .copy{position:absolute;left:120px;top:193px;font-size:12px;color:var(--muted)}
</style>
</head>
<body>

<header class="abs topbar">
  <div class="abs phone">
    <svg width="28" height="28" viewBox="0 0 28 28"><circle cx="14" cy="14" r="12.5" fill="none" stroke="#333" stroke-width="2"/><path d="M10 8c-1 1-1.5 2-1 4 1 3 4 6 7 7 2 .5 3 0 4-1l-2-2.5-2 1c-1.5-.5-3-2-3.5-3.5l1-2z" fill="#333"/></svg>
    <span>Toll Free 1-800-555-0142</span>
  </div>
  <div class="abs cart">
    <svg width="28" height="24" viewBox="0 0 28 24"><path d="M1 3h5l3 12h14l3-9H8" fill="none" stroke="#3b98f0" stroke-width="2.2"/><circle cx="11" cy="20" r="2" fill="#3b98f0"/><circle cx="21" cy="20" r="2" fill="#3b98f0"/></svg>
    <span>0 Item(s)</span>
  </div>
</header>

<div class="abs brand"><span>VitalPawsLife</span><span class="dot"></span></div>

<form class="abs search">
  <input type="text" value="Search" aria-label="Search">
  <button type="button" aria-label="Search"><svg width="18" height="18" viewBox="0 0 18 18"><circle cx="7" cy="7" r="5" fill="none" stroke="#fff" stroke-width="2"/><path d="M11 11l5 5" stroke="#fff" stroke-width="2"/></svg></button>
</form>

<nav class="abs nav">
  <a href="#">Home</a><a href="#">Cats</a><a href="#">Dogs</a><a href="#">Samples</a><a href="#">Join Our Team</a><a href="#">FAQ</a><a href="#">Contact Us</a>
</nav>

<section class="abs slider">
  <div class="photo" role="img" aria-label="Photo of three bulldog puppies lying side by side"></div>
  <span class="arrow" style="left:0"><svg width="12" height="14" viewBox="0 0 12 14"><path d="M9 2L3 7l6 5" fill="none" stroke="#fff" stroke-width="2.5"/></svg></span>
  <span class="arrow" style="right:0"><svg width="12" height="14" viewBox="0 0 12 14"><path d="M3 2l6 5-6 5" fill="none" stroke="#fff" stroke-width="2.5"/></svg></span>
</section>

<aside class="abs promo" style="top:253px">
  <div class="photo" role="img" aria-label="Photo of kittens resting on folded colourful blankets" style="background:linear-gradient(180deg,#fff 20%,#d8cfc4 55%,#c8344a 85%)"></div>
  <div class="band" style="background:var(--teal)"><strong>Cat Food</strong><span>Lorem ipsum dolor sit amet, consectetur adipiscing elit</span><i><svg width="12" height="12" viewBox="0 0 12 12"><path d="M4 2l4 4-4 4" fill="none" stroke="#1cbfbf" stroke-width="2.2"/></svg></i></div>
</aside>
<aside class="abs promo" style="top:477px">
  <div class="photo" role="img" aria-label="Photo of a dog wearing a spa face mask" style="background:linear-gradient(180deg,#fff 10%,#c49a6c 45%,#f4f1ea 70%,#3b98f0)"></div>
  <div class="band" style="background:var(--blue)"><strong>Dag Food</strong><span>Lorem ipsum dolor sit amet, consectetur adipiscing elit</span><i><svg width="12" height="12" viewBox="0 0 12 12"><path d="M4 2l4 4-4 4" fill="none" stroke="#3b98f0" stroke-width="2.2"/></svg></i></div>
</aside>

<article class="abs product" style="top:731px">
  <div class="photo" role="img" aria-label="Photo of a dog eating kibble from a bowl" style="background:linear-gradient(135deg,#f0ece6,#6b4428 45%,#2a1d16 70%,#b99a78)"></div>
  <h3>Quillbrook Farms Dog Food</h3>
  <p>Quillbrook Farms Premium Dog Food is made using ingredients such as premium natural chicken and top quality catfish with the best fruit, vegetables and select farm foods.</p>
  <a class="btn" href="#" style="top:147px">Read More</a>
</article>

<article class="abs product" style="top:1029px">
  <div class="photo" role="img" aria-label="Photo of a tabby cat eating from a bowl" style="background:linear-gradient(135deg,#e8e6e2,#7d7b78 45%,#4a4846 70%,#e5cfa8)"></div>
  <h3>Quillbrook Farms Cat Food</h3>
  <p>Quillbrook Farms Premium Dry Cat Food- Other than treats, your cat eats the same food day in and day out. So the brand of food you feed your cat is important to a long and healthy life.</p>
  <a class="btn" href="#" style="top:149px">Read More</a>
</article>

<article class="abs product" style="top:1324px">
  <div class="photo" role="img" aria-label="Photo of a fish oil supplement bottle held in a hand" style="background:linear-gradient(135deg,#d8a059,#c87a3a 35%,#2d3a55 55%,#dfe9f2 80%)"></div>
  <h3>Aqueltra Fish Oil</h3>
  <p>Aqueltra Omega-3 ultra-refined Fish Oil is scientifically formulated with superior nutritional ingredients to deliver the maximum in Omega-3 nutrition.</p>
  <a class="btn" href="#" style="top:134px">Click Here</a>
</article>

<article class="abs product" style="top:1633px">
  <div class="photo" role="img" aria-label="Photo of a cat food bag showing a kitten" style="background:linear-gradient(180deg,#e9d9a0,#c9a860 40%,#b88a52 65%,#6c8a3a)"></div>
  <h3>Native Select Cat Food</h3>
  <p>Native Select Premium Canned Food is specially formulated to feed along with Quillbrook Farms Premium Dry Food, so your cat can get the benefits of both canned and dry foods. It's not only what is in Native Select that makes it the ultimate canned cat food.</p>
  <a class="btn" href="#" style="top:193px">Click Here</a>
</article>

<aside class="abs panel" style="top:713px;height:596px">
  <div class="head">Pet Products Menu</div>
  <div style="padding:14px 24px 0 24px">
    <h4>Healthy Dog Product Items</h4>
    <ul>
      <li>Dry Dog Food</li><li>Canned Dog Food</li><li>Large Breed Puppy Food</li><li>Weight Loss Food For Dogs</li><li>Nutritional System For Dogs</li><li>Healthy Start Pack for Dogs</li><li>Dog Treats</li><li>Pet Care Supplies for Dogs</li><li>Compare Dog Food Brands</li><li>Dog Supplements</li><li>Dog Gift Baskets</li>
    </ul>
    <h4 style="margin-top:6px">Healthy Cat Product Items</h4>
    <ul>
      <li>Dry Cat Food</li><li>Canned Cat Food</li><li>Nutritional System for Cats</li><li>Healthy Start Pack For Cats</li><li>Cat Treats</li><li>Pet Care Supplies for Cats</li><li>Compare Cat Food Brands</li><li>Cat Supplements</li><li>Cat Gift Baskets</li>
    </ul>
  </div>
</aside>

<aside class="abs panel" style="top:1319px;height:313px;padding:18px 24px 0 24px">
  <h4 style="font-size:18px;margin-bottom:8px">Useful Links</h4>
  <ul>
    <li>Quillbrook Farms FAQ's</li><li>Quillbrook Farms Reviews</li><li>Meet Dr. Mara Felton</li><li>Pet Business Professionals</li><li>Online Pet Home Business</li><li>Holistic Pet Care Blog</li><li>Healthy Pet Newsletter</li><li>Pet Health Insurance</li><li>Pet Resources and Links</li><li>Aqueltra Fish Oil</li><li>ORDER HERE</li>
  </ul>
</aside>

<aside class="abs panel poll" style="top:1653px;height:243px">
  <div class="head">Pet polls</div>
  <div style="padding:18px 18px 0 18px">
    <p>How Safe Is Your Pets Food?</p>
    <label style="margin-top:22px"><i></i>Yes, I have researched my pet's food extensively</label>
    <label style="margin-top:18px"><i></i>No, I never thought about it before now</label>
    <a class="btn" href="#" style="margin:24px 0 0 6px;width:168px;height:43px">Submit</a>
  </div>
</aside>

<div class="abs tile" style="left:119px;background:var(--pink)">
  <svg width="50" height="56" viewBox="0 0 50 56"><rect x="6" y="6" width="38" height="36" rx="4" fill="none" stroke="#fff" stroke-width="3"/><rect x="12" y="12" width="26" height="12" fill="#fff"/><circle cx="15" cy="33" r="3" fill="#fff"/><circle cx="35" cy="33" r="3" fill="#fff"/><rect x="10" y="42" width="6" height="8" fill="#fff"/><rect x="34" y="42" width="6" height="8" fill="#fff"/></svg>
  <div><strong>FREE SHIPPING</strong><span>ON ORDERS</span></div>
</div>
<div class="abs tile" style="left:456px;background:var(--teal)">
  <svg width="46" height="56" viewBox="0 0 46 56"><path d="M10 6c-6 4-8 10-4 20 5 12 14 22 26 26 6 2 10 0 12-4l-8-9-6 4c-6-3-11-9-14-16l5-6z" fill="#fff"/></svg>
  <div><strong>ORDER ONLINE</strong><span>LIVE SUPPORT</span></div>
</div>
<div class="abs tile" style="left:788px;background:var(--blue)">
  <svg width="56" height="50" viewBox="0 0 56 50"><path d="M4 20L28 4l24 16v26H4z" fill="none" stroke="#fff" stroke-width="3"/><path d="M4 20l24 16 24-16" fill="none" stroke="#fff" stroke-width="3"/><path d="M18 18h20M18 24h20" stroke="#fff" stroke-width="2.5"/></svg>
  <div><strong>NEWSLETTER</strong><span>SUBSCRIBE HEALTHY<br>PET NEWSLETTER</span></div>
</div>

<footer class="abs footer">
  <h5 style="left:121px">INFORMATION</h5>
  <ul style="left:120px"><li>About Us</li><li>Delivery Information</li><li>Privacy Policy</li><li>Terms &amp; Conditions</li></ul>
  <h5 style="left:330px">CUSTOMER SERVICE</h5>
  <ul style="left:331px"><li>Contact Us</li><li>Returns</li><li>Site Map</li></ul>
  <h5 style="left:560px">MY ACCOUNT</h5>
  <ul style="left:561px"><li>My Account</li><li>Order History</li><li>Wish List</li><li>Newsletter</li></ul>
  <h5 style="left:751px">FOLLOW US</h5>
  <div class="social"><i></i><i></i><i></i><i></i></div>
  <div class="badge"></div>
  <p class="copy">© 2004 - 2014 VitalPawsLife.com. All Rights Reserved.</p>
</footer>

</body>
</html>
```